Turning fine print into insight is a show dedicated to helping plan fiduciaries close the gap between ERISA participant disclosures and employees, understanding, and attaining actual knowledge of their plan.

Target Market(s)

Retirement Plan Sponsors

Industry/Entity Type

Financial

Colors
0054AA
0677BA
7BADD7
CADEEF
E8F1F8

Requirements
Must have
• Turning Fine Print Into Insight

```html
<!DOCTYPE html>
<html lang="en">
<head>
<meta charset="utf-8">
<title>Turning Fine Print Into Insight – Podcast Cover</title>
<link href="https://fonts.googleapis.com/css2?family=Saira+Extra+Condensed:wght@700&family=Saira+Condensed:wght@600&family=Archivo+Black&display=swap" rel="stylesheet">
<style>
  :root {
    --deep-blue: #0054AA;
    --brand-blue: #0677BA;
    --cover-blue: #1178BE;
    --sky-blue: #7BADD7;
    --pale-blue: #CADEEF;
    --mist: #E8F1F8;
    --white: #FFFFFF;
    --photo-light: #9a9ea3;
    --photo-dark: #1f2226;
  }
  html, body {
    margin: 0;
    padding: 0;
    width: 1200px;
    height: 1200px;
    overflow: hidden;
    background: var(--pale-blue);
  }
  .cover {
    display: block;
    width: 1200px;
    height: 1200px;
  }
  .title-line {
    font-family: "Saira Extra Condensed", "Arial Narrow", sans-serif;
    font-weight: 700;
    fill: var(--white);
  }
  .podcast-tag {
    font-family: "Archivo Black", "Arial Black", sans-serif;
    fill: var(--brand-blue);
    font-size: 50px;
  }
  .host-line {
    font-family: "Saira Condensed", "Arial Narrow", sans-serif;
    font-weight: 600;
    fill: var(--white);
    font-size: 96px;
  }
</style>
</head>
<body>
<svg class="cover" viewBox="0 0 1200 1200" xmlns="http://www.w3.org/2000/svg">
  <defs>
    <linearGradient id="host-photo-tone" x1="0" y1="0" x2="0" y2="1">
      <stop offset="0" stop-color="var(--photo-light)"/>
      <stop offset="0.45" stop-color="#7c8085"/>
      <stop offset="0.55" stop-color="#2e3136"/>
      <stop offset="1" stop-color="var(--photo-dark)"/>
    </linearGradient>
    <linearGradient id="long-shadow" x1="0" y1="0" x2="1" y2="1">
      <stop offset="0" stop-color="var(--deep-blue)" stop-opacity="0.5"/>
      <stop offset="1" stop-color="var(--deep-blue)" stop-opacity="0.1"/>
    </linearGradient>
    <clipPath id="photo-clip">
      <ellipse cx="838" cy="400" rx="200" ry="270"/>
      <path d="M408,1200 C412,1060 425,960 460,900 C530,790 620,700 700,610 C780,630 880,640 960,600 C1040,590 1120,610 1200,640 L1200,1200 Z"/>
    </clipPath>
  </defs>

  <!-- cover base -->
  <rect class="cover-base" x="0" y="0" width="1200" height="1200" fill="var(--cover-blue)"/>

  <!-- long shadow cast by the title -->
  <polygon class="title-shadow" points="505,138 720,330 720,1200 560,1200 430,1060 148,830 148,138" fill="url(#long-shadow)"/>

  <!-- inner frame -->
  <polyline class="inner-frame" points="903,58 58,58 58,1141 416,1141" fill="none" stroke="var(--white)" stroke-width="5"/>

  <!-- white diagonal band -->
  <polygon class="diagonal-band" points="924,0 1141,0 840,1200 740,1200" fill="var(--white)"/>

  <!-- host photo area -->
  <g class="host-photo" role="img" aria-label="Black and white portrait of the podcast host in a dark suit and tie">
    <rect x="400" y="120" width="800" height="1080" fill="url(#host-photo-tone)" clip-path="url(#photo-clip)"/>
  </g>

  <!-- band continuing as blue tint over the photo -->
  <polygon class="diagonal-band-tint" points="924,0 1141,0 840,1200 740,1200" fill="var(--brand-blue)" opacity="0.85" clip-path="url(#photo-clip)"/>

  <!-- title -->
  <text class="title-line" x="145" y="250" font-size="160" textLength="360" lengthAdjust="spacingAndGlyphs">TURNING</text>
  <text class="title-line" x="145" y="350" font-size="114" textLength="360" lengthAdjust="spacingAndGlyphs">FINE PRINT</text>
  <text class="title-line" x="145" y="590" font-size="314" textLength="360" lengthAdjust="spacingAndGlyphs">INTO</text>
  <text class="title-line" x="145" y="821" font-size="300" textLength="360" lengthAdjust="spacingAndGlyphs">INSIGHT</text>

  <!-- podcast tag -->
  <rect class="podcast-tag-box" x="148" y="849" width="349" height="64" fill="var(--sky-blue)"/>
  <text class="podcast-tag" x="165" y="898" textLength="321" lengthAdjust="spacing">PODCAST</text>

  <!-- host -->
  <text class="host-line" x="143" y="1073" textLength="659" lengthAdjust="spacing">WITH DALE MARSH</text>
</svg>
</body>
</html>
```